Summer Classical Chamber Music Festival

We are a summer classical music festival that takes place in the South of France. We are looking for a graphic that we can use as a basis for our concert posters, concert programs, banners and other marketing materials this season. Essentially, something to which we can just add dates and text. I am attaching some of our previous seasons' posters, as well as other designs (examples) that we admire and try to model. The design should communicate the region (Cote D'Azur), summer, classical music and class (style). For reference, our website is www.velmorafestival.com

```html
<!DOCTYPE html>
<html lang="fr">
<head>
<meta charset="utf-8">
<title>Festival de Musique Velmora</title>
<link href="https://fonts.googleapis.com/css2?family=Montserrat:wght@300;400;600&family=Smokum&family=Oswald:wght@300;400&display=swap" rel="stylesheet">
<style>
  :root {
    --paper: #fbfaf7;
    --ink: #111111;
    --ochre: #eeb35a;
    --sun: #f3cf62;
    --teal: #6cc9d6;
    --sky: #a9dde4;
    --sketch: #c9b9a4;
  }
  * { margin: 0; padding: 0; box-sizing: border-box; }
  html, body { width: 903px; height: 1200px; overflow: hidden; background: var(--paper); }
  .poster {
    position: relative; width: 903px; height: 1200px; overflow: hidden;
    background: var(--paper); color: var(--ink);
    font-family: "Montserrat", sans-serif;
  }
  .wash { position: absolute; border-radius: 50%; filter: blur(28px); }
  .wash--sun { left: 330px; top: 40px; width: 560px; height: 420px;
    background: radial-gradient(circle, var(--sun) 0%, var(--ochre) 55%, transparent 75%); opacity: .75; }
  .wash--ochre { left: 0; top: 260px; width: 520px; height: 560px;
    background: radial-gradient(circle, var(--ochre) 0%, transparent 70%); opacity: .55; }
  .wash--teal { left: 380px; top: 640px; width: 560px; height: 560px;
    background: radial-gradient(circle, var(--teal) 0%, var(--sky) 45%, transparent 72%); opacity: .75; }
  .illustration {
    position: absolute; left: 20px; top: 230px; width: 880px; height: 480px;
    background: radial-gradient(ellipse at 40% 50%, rgba(150,130,110,.35), rgba(201,185,164,.12) 60%, transparent 80%);
  }
  .landscape {
    position: absolute; left: 0; bottom: 0; width: 903px; height: 170px;
    background: linear-gradient(to bottom, transparent, rgba(108,201,214,.45) 45%, rgba(120,190,200,.55));
  }
  .edition { position: absolute; top: 52px; left: 0; width: 903px; text-align: center; font-size: 19px; font-weight: 400; }
  .festival { position: absolute; top: 86px; right: 66px; font-size: 55px; font-weight: 300; letter-spacing: 1px; line-height: 1; }
  .name { position: absolute; top: 158px; right: 60px; font-family: "Smokum", serif; font-size: 150px; line-height: 1; }
  .place { position: absolute; top: 320px; right: 66px; font-size: 34px; font-weight: 300; }
  .place strong { font-weight: 600; }
  .month { position: absolute; top: 630px; left: 50px; font-family: "Smokum", serif; font-size: 86px; line-height: 1; }
  .dates { position: absolute; top: 728px; left: 54px; list-style: none; }
  .date { display: flex; align-items: center; height: 73px; }
  .date__day { width: 76px; font-family: "Oswald", sans-serif; font-size: 46px; font-weight: 300; }
  .date__info { font-size: 12.5px; line-height: 1.3; font-weight: 400; }
  .headline { position: absolute; right: 66px; text-align: right; font-family: "Smokum", serif; line-height: 1; }
  .headline--concerts { top: 650px; font-size: 72px; }
  .headline--musique { top: 712px; font-size: 118px; }
  .headline--classique { top: 826px; font-size: 72px; }
  .receptions { position: absolute; top: 910px; right: 66px; text-align: right; font-size: 19px; font-weight: 300; line-height: 1.25; }
  .stamp { position: absolute; left: 648px; top: 982px; width: 170px; height: 170px; }
</style>
</head>
<body>
<main class="poster">
  <div class="wash wash--ochre"></div>
  <div class="wash wash--sun"></div>
  <div class="wash wash--teal"></div>
  <div class="illustration" role="img" aria-label="Pencil sketch of a violinist playing, with a small bird perched on the violin scroll"></div>
  <div class="landscape" role="img" aria-label="Watercolour mountain lake with pine trees reflected in the water"></div>

  <p class="edition">7ème Edition</p>
  <h1 class="festival">FESTIVAL DE MUSIQUE</h1>
  <p class="name">“VELMORA”</p>
  <p class="place">À <strong>VALDEBLORE</strong></p>

  <h2 class="month">JUILLET</h2>
  <ul class="dates">
    <li class="date"><span class="date__day">04</span><span class="date__info">21h<br>Soirée d'Ouverture<br>Eglise de LA BOLLINE</span></li>
    <li class="date"><span class="date__day">06</span><span class="date__info">21h Eglise<br>de LA BOLLINE</span></li>
    <li class="date"><span class="date__day">09</span><span class="date__info">21h Eglise<br>de LA BOLLINE</span></li>
    <li class="date"><span class="date__day">12</span><span class="date__info">21h Eglise<br>de ST. DALMAS</span></li>
    <li class="date"><span class="date__day">13</span><span class="date__info">21h<br>de LA BOLLINE</span></li>
    <li class="date"><span class="date__day">14</span><span class="date__info">15h &amp; 21h<br>Gala de Clôture<br>Eglise de LA BOLLINE</span></li>
  </ul>

  <p class="headline headline--concerts">CONCERTS</p>
  <p class="headline headline--musique">MUSIQUE</p>
  <p class="headline headline--classique">CLASSIQUE</p>
  <p class="receptions">RÉCEPTIONS OFFERTES<br>APRÈS LES CONCERTS</p>

  <svg class="stamp" viewBox="0 0 170 170" aria-label="Entrée gratuite">
    <circle cx="85" cy="85" r="80" fill="none" stroke="#111" stroke-width="5"/>
    <circle cx="85" cy="85" r="71" fill="none" stroke="#111" stroke-width="2"/>
    <g transform="rotate(15 85 85)" font-family="Oswald, sans-serif" font-weight="400" fill="#111" text-anchor="middle">
      <text x="85" y="82" font-size="34">ENTRÉE</text>
      <text x="85" y="112" font-size="26">GRATUITE</text>
    </g>
  </svg>
</main>
</body>
</html>
```